Sydney law firm, Prestwicks Solicitors, needs a flyer design!

We need a flyer design for our law firm which has been operating in Sydney for over 35 years. We want to send the flyer out to potential clients and also to existing clients to let them know the range of services that we provide. Our corporate colours are white, red and black and we would like these incorporated somewhat. The final design should be clean, modern and professional.

We would like the design to fit a double sided flyer approx. 210mm high x 100mm wide.

Industry/Entity Type

Law Firm

Font styles to use
Serif
Sans Serif

Colors
eb2026
ffffff

Requirements
Must have
• Details needed on the flyer are:
• Prestwicks Solicitors
• 3/82 Carradine Street, Liverpool, NSW 2170
• (02) 9418 3562
• www.prestwickssolicitors-example.com.au
• info@prestwickssolicitors-example.com.au
• Our areas of practice include:
• Property Law
• Conveyancing
• Leases
• Criminal Law
• Family Law
• Litigation and Dispute Resolution
• Company Law
• Wills and Estates
• Powers of Attorney and Guardianship
Should not have
• a picture of scales or a picture of a gavel

```html
<!DOCTYPE html>
<html lang="en">
<head>
<meta charset="utf-8">
<title>Prestwicks Solicitors – Flyer</title>
<link href="https://fonts.googleapis.com/css2?family=Source+Sans+3:wght@400;600;700&display=swap" rel="stylesheet">
<style>
  :root {
    --brand-red: #a52226;
    --brand-red-dark: #8e1b1f;
    --ink: #222222;
    --body-ink: #2b2b2b;
    --grey-light: #f1f1f1;
    --grey-mid: #d6d6d6;
    --grey-dark: #b9b9b9;
    --white: #ffffff;
    --canvas: #ffffff;
  }
  * { box-sizing: border-box; margin: 0; padding: 0; }
  html, body {
    width: 1200px; height: 848px; overflow: hidden;
    background: var(--canvas);
    font-family: "Source Sans 3", "Myriad Pro", Arial, sans-serif;
  }
  .canvas { position: relative; width: 1200px; height: 848px; }

  .flyer {
    position: absolute; top: 53px; width: 355px; height: 745px;
    background: linear-gradient(180deg, var(--grey-mid) 0%, var(--grey-light) 60%, var(--white) 100%);
    box-shadow: 3px 4px 8px rgba(0,0,0,0.28);
    overflow: hidden;
  }
  .flyer--front { left: 230px; }
  .flyer--back { left: 642px; }

  .flyer__header {
    position: absolute; top: 0; left: 0; width: 355px; height: 140px; z-index: 2;
  }
  .brand {
    position: absolute; top: 20px; right: 20px; z-index: 3;
    text-align: center; color: var(--ink); font-weight: 600;
  }
  .brand__name { display: block; font-size: 29px; line-height: 1; letter-spacing: 0.5px; }
  .brand__tag { display: block; font-size: 10px; letter-spacing: 5.6px; margin-top: 4px; padding-left: 5px; }

  .flyer__photo {
    position: absolute; top: 100px; left: 0; width: 355px; height: 370px; z-index: 1;
  }
  .flyer--front .flyer__photo {
    background: linear-gradient(135deg, #eef1f3 0%, #dfe8f2 45%, #c9d8ea 70%, #d8c4a8 100%);
  }
  .flyer--back .flyer__photo {
    background: linear-gradient(90deg, #cfd6dc 0%, #8d97a2 30%, #5d6670 55%, #9aa3ac 80%, #c9c2b6 100%);
  }

  .flyer__divider {
    position: absolute; top: 440px; left: 0; width: 355px; height: 80px; z-index: 2;
  }

  .flyer__content {
    position: absolute; top: 508px; left: 14px; right: 14px; z-index: 3;
  }
  .headline {
    color: var(--brand-red); font-weight: 700; font-size: 30px;
    line-height: 1.08; letter-spacing: -0.3px;
  }
  .intro { margin-top: 12px; width: 280px; }
  .intro p { font-size: 12.4px; line-height: 1.3; color: var(--body-ink); margin-bottom: 8px; }

  .services {
    display: flex; gap: 14px; margin-top: 10px; list-style: none;
  }
  .services ul { list-style: none; }
  .services li {
    position: relative; padding-left: 14px;
    font-size: 12px; line-height: 1.22; color: var(--body-ink);
  }
  .services li::before {
    content: ""; position: absolute; left: 2px; top: 6px;
    width: 3px; height: 3px; border-radius: 50%; background: var(--body-ink);
  }
  .services__col--a { width: 148px; }
  .services__col--b { width: 150px; }

  .cta {
    position: absolute; right: 0; top: 667px; z-index: 3;
    width: 190px; height: 25px; padding-left: 20px;
    background: linear-gradient(90deg, rgba(200,200,200,0) 0%, var(--grey-dark) 14%, #c6c6c6 100%);
    border-radius: 14px 0 0 0;
    font-weight: 700; font-size: 16px; line-height: 25px; color: var(--ink);
  }

  .flyer__footer {
    position: absolute; left: 0; bottom: 0; width: 355px; height: 53px; z-index: 3;
    background: var(--brand-red);
    color: var(--white); text-align: center;
    font-weight: 600; font-size: 8.6px; line-height: 11px;
    padding-top: 10px;
  }
</style>
</head>
<body>
<div class="canvas">

  <!-- Front side -->
  <section class="flyer flyer--front">
    <svg class="flyer__header" viewBox="0 0 355 140" aria-hidden="true">
      <defs>
        <linearGradient id="headGrey" x1="0" y1="0" x2="0" y2="1">
          <stop offset="0" stop-color="#c9c9c9"/>
          <stop offset="0.5" stop-color="#ececec"/>
          <stop offset="1" stop-color="#d4d4d4"/>
        </linearGradient>
      </defs>
      <path d="M0 0 H355 V108 Q200 96 0 124 Z" fill="url(#headGrey)"/>
      <path d="M0 42 C120 52 240 92 355 74" fill="none" stroke="#ffffff" stroke-width="6"/>
      <path d="M0 60 C60 62 110 74 140 92 C90 95 40 99 0 102 Z" fill="var(--brand-red)"/>
      <path d="M0 124 Q200 96 355 108" fill="none" stroke="#ffffff" stroke-width="3"/>
    </svg>
    <div class="brand">
      <span class="brand__name">PRESTWICKS</span>
      <span class="brand__tag">SOLICITORS</span>
    </div>

    <div class="flyer__photo" role="img" aria-label="Photo of a smiling solicitor shaking hands with a client across a desk"></div>

    <svg class="flyer__divider" viewBox="0 0 355 80" aria-hidden="true">
      <defs>
        <linearGradient id="divGrey" x1="0" y1="0" x2="0" y2="1">
          <stop offset="0" stop-color="#cfcfcf"/>
          <stop offset="1" stop-color="#dcdcdc"/>
        </linearGradient>
      </defs>
      <path d="M0 14 Q180 -6 355 22 V80 H0 Z" fill="url(#divGrey)"/>
      <path d="M0 14 Q180 -6 355 22" fill="none" stroke="#ffffff" stroke-width="5"/>
      <path d="M200 44 C260 34 310 28 355 26 V50 C300 50 250 48 200 44 Z" fill="var(--brand-red)"/>
      <path d="M0 40 Q150 18 355 30" fill="none" stroke="#ffffff" stroke-width="2" opacity="0.7"/>
    </svg>

    <div class="flyer__content">
      <h1 class="headline">Our clients really<br>do come first!</h1>
      <div class="intro">
        <p>Prestwicks Solicitors is a private law firm based in Liverpool that has been servicing the Sydney area for over 35 years.</p>
        <p>With a dedicated, professional and friendly team we pride ourselves on delivery an exceptional legal service to our clients.</p>
      </div>
    </div>

    <footer class="flyer__footer">
      3/82 Carradine Street, Liverpool, NSW 2170<br>
      Phone: (02) 9418 3562 | Email: info@prestwickssolicitors-example.com.au<br>
      www.prestwickssolicitors-example.com.au
    </footer>
  </section>

  <!-- Back side -->
  <section class="flyer flyer--back">
    <svg class="flyer__header" viewBox="0 0 355 140" aria-hidden="true">
      <path d="M0 0 H355 V108 Q200 96 0 124 Z" fill="url(#headGrey)"/>
      <path d="M0 42 C120 52 240 92 355 74" fill="none" stroke="#ffffff" stroke-width="6"/>
      <path d="M0 60 C60 62 110 74 140 92 C90 95 40 99 0 102 Z" fill="var(--brand-red)"/>
      <path d="M0 124 Q200 96 355 108" fill="none" stroke="#ffffff" stroke-width="3"/>
    </svg>
    <div class="brand">
      <span class="brand__name">PRESTWICKS</span>
      <span class="brand__tag">SOLICITORS</span>
    </div>

    <div class="flyer__photo" role="img" aria-label="Photo of a confident solicitor with arms crossed, two colleagues in suits behind her"></div>

    <svg class="flyer__divider" viewBox="0 0 355 80" aria-hidden="true">
      <path d="M0 14 Q180 -6 355 22 V80 H0 Z" fill="url(#divGrey)"/>
      <path d="M0 14 Q180 -6 355 22" fill="none" stroke="#ffffff" stroke-width="5"/>
      <path d="M200 44 C260 34 310 28 355 26 V50 C300 50 250 48 200 44 Z" fill="var(--brand-red)"/>
      <path d="M0 40 Q150 18 355 30" fill="none" stroke="#ffffff" stroke-width="2" opacity="0.7"/>
    </svg>

    <div class="flyer__content">
      <h2 class="headline">Over 35 years of service<br>you can trust:</h2>
      <div class="services">
        <ul class="services__col--a">
          <li>Property Law</li>
          <li>Conveyancing</li>
          <li>Leases</li>
          <li>Criminal Law</li>
          <li>Family Law</li>
          <li>Litigation and Dispute Resolution</li>
        </ul>
        <ul class="services__col--b">
          <li>Company Law</li>
          <li>Wills and Estates</li>
          <li>Powers of Attorney and Guardianship</li>
        </ul>
      </div>
    </div>

    <div class="cta">Call us today!</div>

    <footer class="flyer__footer">
      3/82 Carradine Street, Liverpool, NSW 2170<br>
      Phone: (02) 9418 3562 | Email: info@prestwickssolicitors-example.com.au<br>
      www.prestwickssolicitors-example.com.au
    </footer>
  </section>

</div>
</body>
</html>
```